Hearth & Keg Room requires web site design - Casual restaurant

Need website designed for re-branding of Restaurant based in Fort Morgan, Colorado. We offer a wide variety of American cuisine in a casual, rustic atmosphere. We're offering 16 craft beers on draft, as well as a full service bar, and modern, interesting menu selections in a friendly, fun and energetic environment, with an emphasis on superior customer service and high quality, locally sourced food. We are a family, and community service oriented establishment. The website design should convey a welcoming sense, "simplicity", yet sophisticated - without pretentiousness. The website should effectively convey our "home style" relaxed atmosphere, as well as our casual character.

Business Hours: Sunday - Thursday, 11am-10pm / Friday & Saturday, 11am-11am

The Dunlo Hearth & Keg Room
2736 Pennick Road
Kestrel Bend, Colorado 80799
B: (970) 555-0173

WEBSITE ADDRESS: thedunlokegroom.com

Target Market(s)

Young Adults
Families
Blue and White Collar Americans
Senior Citizens
Small town location, appeal to everyone

Industry/Entity Type

American Restaurant

Contact Information for Business Card

Marcus T Ellery
Food & Beverage Director
2736 Pennick Road
B: (970) 555-0173
M: (231) 555-0148
mtellery@dunlokegroom.com
www.thedunlokegroom.com
***Use logo in uploaded files
***Open to single OR double sided
*** I will have additional names and information to add to this, for other employees.

Coding

Coded - Design and coding required

Number of Pages Required

5+ page

Font styles to use
Serif
Sans Serif
Decorative
Other font styles liked:
• Calafornian FB,

Requirements
Must have
• Home/Welcome Page
• Menu Page/Online Ordering Ready
• About Us/Contact Us page
• Catering/Private Events/Banquets Advertising section
• Ability to link to Facebook/TripAdvisor/Yelp/Instagram etc.
• Logo uploaded, reference for colors as well.
Nice to have
• About craft beer page
• Our Story/Bio section
• Photo Gallery
• Employment/Apply section
Should not have
• We are NOT a "fine dining" restaurant... think casual...

```html
<!DOCTYPE html>
<html lang="en">
<head>
<meta charset="utf-8">
<title>The Dunlo Hearth &amp; Keg Room</title>
<link rel="stylesheet" href="https://fonts.googleapis.com/css2?family=Roboto:wght@400;500;700&family=Open+Sans:wght@400;600;700&family=Lato:wght@700;900&family=Playball&display=swap">
<style>
  :root {
    --brand: #a63b10;
    --brand-text: #a8410f;
    --ink: #2b2b2b;
    --body: #666666;
    --nav: #444444;
    --muted: #777777;
    --band: #efefef;
    --footer: #e9ad80;
    --white: #ffffff;
    --rule: rgba(255,255,255,0.45);
  }
  * { box-sizing: border-box; margin: 0; padding: 0; }
  html, body { width: 1200px; height: 2326px; overflow: hidden; }
  body { position: relative; background: var(--white); font-family: "Open Sans", Arial, sans-serif; color: var(--body); }

  .site-header { position: absolute; left: 0; top: 0; width: 1200px; height: 124px; background: var(--white); }
  .brand-name { position: absolute; left: 81px; top: 38px; font-family: "Roboto", Arial, sans-serif; font-weight: 700; color: var(--ink); font-size: 18px; line-height: 22px; }
  .utility-links { position: absolute; right: 77px; top: 10px; display: flex; font-size: 15px; color: var(--muted); }
  .utility-links span { display: flex; align-items: center; gap: 7px; padding: 0 17px; border-left: 1px solid #dddddd; height: 24px; }
  .utility-links span:first-child { border-left: none; }
  .utility-links svg { width: 14px; height: 14px; fill: #8a8a8a; }
  .main-nav { position: absolute; right: 77px; top: 68px; display: flex; gap: 29px; font-family: "Roboto", Arial, sans-serif; font-size: 16px; color: var(--nav); }
  .main-nav .current { color: var(--brand-text); }

  .hero { position: absolute; left: 0; top: 124px; width: 1200px; height: 574px;
    background: radial-gradient(ellipse at 50% 45%, #9a6437 0%, #7a4622 45%, #4e2a12 100%); }
  .hero-photo { position: absolute; inset: 0; background:
    radial-gradient(circle at 12% 30%, rgba(200,170,80,0.45) 0 14%, transparent 15%),
    radial-gradient(circle at 62% 17%, rgba(226,170,40,0.55) 0 11%, transparent 12%),
    radial-gradient(circle at 90% 22%, rgba(160,90,50,0.5) 0 12%, transparent 13%),
    radial-gradient(circle at 88% 75%, rgba(230,180,110,0.45) 0 15%, transparent 16%),
    radial-gradient(circle at 8% 75%, rgba(200,140,80,0.45) 0 15%, transparent 16%); }
  .hero-copy { position: absolute; left: 0; width: 1200px; top: 280px; text-align: center; color: var(--white); }
  .hero-tagline { font-family: "Playball", cursive; font-size: 30px; line-height: 36px; }
  .hero-title { margin-top: 6px; font-family: "Lato", Arial, sans-serif; font-weight: 900; font-size: 46px; line-height: 53px; }
  .hero-cta { position: absolute; left: 499px; top: 459px; width: 202px; height: 48px; border-radius: 24px; background: var(--white); color: var(--brand-text); font-family: "Open Sans", Arial, sans-serif; font-weight: 700; font-size: 17px; display: flex; align-items: center; justify-content: center; }

  .btn { position: absolute; display: flex; align-items: center; justify-content: center; gap: 8px; background: var(--brand); color: var(--white); border-radius: 25px; font-family: "Open Sans", Arial, sans-serif; font-size: 18px; height: 50px; }
  .btn svg { width: 13px; height: 13px; stroke: var(--white); fill: none; stroke-width: 2; }

  .welcome { position: absolute; left: 0; top: 698px; width: 1200px; height: 397px; }
  .welcome h1 { position: absolute; left: 80px; top: 50px; font-family: "Roboto", Arial, sans-serif; font-weight: 400; font-size: 41px; line-height: 50px; color: var(--ink); }
  .welcome h1 strong { display: block; font-weight: 400; color: var(--brand-text); font-size: 42px; }
  .welcome p { position: absolute; left: 80px; top: 167px; width: 590px; font-size: 15.5px; line-height: 25.5px; }
  .welcome .btn { left: 78px; top: 294px; width: 170px; }
  .welcome-mark { position: absolute; left: 700px; top: 138px; width: 424px; text-align: center; font-family: "Roboto", Arial, sans-serif; font-weight: 700; color: var(--ink); font-size: 44px; line-height: 54px; }

  .story { position: absolute; left: 0; top: 1095px; width: 1200px; height: 347px; background: var(--band); text-align: center; }
  .section-title { font-family: "Roboto", Arial, sans-serif; font-weight: 400; font-size: 41px; color: var(--ink); }
  .section-title em { font-style: normal; color: var(--brand-text); }
  .story .section-title { position: absolute; left: 0; width: 1200px; top: 46px; }
  .story p { position: absolute; left: 115px; width: 970px; top: 119px; font-size: 15px; line-height: 25.5px; }
  .story .btn { left: 515px; top: 243px; width: 170px; }

  .gallery { position: absolute; left: 0; top: 1442px; width: 1200px; height: 530px; text-align: center; }
  .gallery .section-title { position: absolute; left: 0; width: 1200px; top: 47px; color: var(--brand-text); }
  .gallery p { position: absolute; left: 100px; width: 1000px; top: 120px; font-size: 15px; line-height: 25.5px; }
  .gallery-strip { position: absolute; left: 0; top: 212px; width: 1200px; height: 175px; display: flex; }
  .gallery-strip div { flex: 1; }
  .shot-pizza { background: linear-gradient(135deg, #3a2a1e, #7a3c22 55%, #2a211b); }
  .shot-wrap { background: linear-gradient(135deg, #2e3438, #5b5f5e 55%, #c9b8a8); }
  .shot-spoon { background: radial-gradient(ellipse at 60% 55%, #e8dccb 0 22%, #2a1a12 45%, #120c08); }
  .shot-dough { background: linear-gradient(135deg, #4a2a1a, #a54a28 50%, #d9c3a5); }
  .gallery .btn { left: 521px; top: 434px; width: 158px; height: 48px; font-size: 18px; }

  .site-footer { position: absolute; left: 0; top: 1981px; width: 1200px; height: 345px; background: var(--footer); color: var(--white); text-align: center; }
  .contact-item { position: absolute; top: 17px; width: 400px; font-size: 15px; line-height: 24px; }
  .contact-icon { width: 62px; height: 62px; margin: 0 auto 14px; border: 2px solid var(--white); border-radius: 50%; display: flex; align-items: center; justify-content: center; }
  .contact-icon svg { width: 24px; height: 24px; fill: var(--white); }
  .footer-rule { position: absolute; left: 78px; right: 78px; top: 160px; height: 1px; background: var(--rule); }
  .footer-name { position: absolute; left: 0; width: 1200px; top: 190px; font-family: "Roboto", Arial, sans-serif; font-weight: 700; color: var(--ink); font-size: 22px; line-height: 27px; }
  .copyright { position: absolute; left: 0; width: 1200px; top: 292px; font-size: 15px; }
  .copyright b { font-weight: 700; }
</style>
</head>
<body>

<header class="site-header">
  <div class="brand-name">The Dunlo<br>Hearth &amp; Keg Room</div>
  <div class="utility-links">
    <span><svg viewBox="0 0 16 16"><path d="M1 7h8V4l5 4-5 4V9H1z"/></svg>Signin</span>
    <span><svg viewBox="0 0 16 16"><path d="M3 7h10v8H3z M5 7V5a3 3 0 0 1 6 0v2h-1.6V5a1.4 1.4 0 0 0-2.8 0v2z"/></svg>Login</span>
    <span><svg viewBox="0 0 16 16"><path d="M0 2h3l2 8h8l2-6H5V3h11l-3 9H4L2 3.5H0z M5 13.5a1.3 1.3 0 1 0 .01 0z M12 13.5a1.3 1.3 0 1 0 .01 0z"/></svg>My Cart</span>
  </div>
  <nav class="main-nav">
    <span class="current">Home</span>
    <span>About Us</span>
    <span>Menu</span>
    <span>About Craft Beer</span>
    <span>Private Events</span>
    <span>Gallery</span>
    <span>Employment</span>
    <span>Contact Us</span>
  </nav>
</header>

<section class="hero">
  <div class="hero-photo" role="img" aria-label="Rustic wooden table spread with pasta, bread, pretzels, lasagna, cookies and pizza slices"></div>
  <div class="hero-copy">
    <div class="hero-tagline">Only Using the Finest Ingredients</div>
    <div class="hero-title">The Dunlo<br>Hearth &amp; Keg Room</div>
  </div>
  <div class="hero-cta">CONTACT US NOW</div>
</section>

<section class="welcome">
  <h1>Welcome To <strong>The Dunlo Hearth &amp; Keg Room</strong></h1>
  <p>Lorem Ipsum is simply dummy text of the printing and typesetting industry. Lorem Ipsum has been the industry's standard dummy text ever since the 1500s, when an unknown printer took a galley of type and scrambled it to make a type specimen book. It has survived not only five centuries, but also the leap into...</p>
  <div class="btn">READ MORE <svg viewBox="0 0 14 14"><path d="M2 2l5 5-5 5M7 2l5 5-5 5"/></svg></div>
  <div class="welcome-mark">The Dunlo<br>Hearth &amp; Keg Room</div>
</section>

<section class="story">
  <h2 class="section-title">Our <em>Story</em></h2>
  <p>Lorem Ipsum is simply dummy text of the printing and typesetting industry. Lorem Ipsum has been the industry's standard dummy text ever since the 1500s, when an unknown printer took a galley of type and scrambled it to make a type specimn book. It has survived not only five centuries, but also the leap into electronic type setting, remaining essentially unchanged.<br>It was popularised in the 1960s with...</p>
  <div class="btn">READ MORE <svg viewBox="0 0 14 14"><path d="M2 2l5 5-5 5M7 2l5 5-5 5"/></svg></div>
</section>

<section class="gallery">
  <h2 class="section-title">Gallery</h2>
  <p>Lorem Ipsum is simply dummy text of the printing and typesetting industry. Lorem Ipsum has been the industry's standard dummy text ever since the 1500s, when an unknown printer took a galley of type.</p>
  <div class="gallery-strip">
    <div class="shot-pizza" role="img" aria-label="Overhead view of pizzas and side dishes on a dark table"></div>
    <div class="shot-wrap" role="img" aria-label="Grilled wraps with dried chilies on a slate surface"></div>
    <div class="shot-spoon" role="img" aria-label="Layered pasta bite served on a white spoon"></div>
    <div class="shot-dough" role="img" aria-label="Pizza dough with tomatoes, peppers and mushrooms"></div>
  </div>
  <div class="btn">SHOW ALL <svg viewBox="0 0 14 14"><path d="M2 2l5 5-5 5M7 2l5 5-5 5"/></svg></div>
</section>

<footer class="site-footer">
  <div class="contact-item" style="left:73px">
    <div class="contact-icon"><svg viewBox="0 0 24 24"><path d="M12 1a7.5 7.5 0 0 0-7.5 7.5C4.5 14 12 23 12 23s7.5-9 7.5-14.5A7.5 7.5 0 0 0 12 1zm0 10.3a2.8 2.8 0 1 1 0-5.6 2.8 2.8 0 0 1 0 5.6z"/></svg></div>
    The Dunlo Hearth &amp; Keg Room, 2736 Pennick Road<br>Kestrel Bend, Colorado 80799
  </div>
  <div class="contact-item" style="left:400px">
    <div class="contact-icon"><svg viewBox="0 0 24 24"><path d="M6.6 10.8a15.2 15.2 0 0 0 6.6 6.6l2.2-2.2a1 1 0 0 1 1-.25 11.4 11.4 0 0 0 3.6.57 1 1 0 0 1 1 1V20a1 1 0 0 1-1 1A17 17 0 0 1 3 4a1 1 0 0 1 1-1h3.5a1 1 0 0 1 1 1c0 1.25.2 2.45.57 3.57a1 1 0 0 1-.25 1z"/></svg></div>
    800-555-0192
  </div>
  <div class="contact-item" style="left:756px">
    <div class="contact-icon"><svg viewBox="0 0 24 24"><path d="M2 5h20v2.2l-10 6.3L2 7.2z M2 9.4l10 6.3 10-6.3V19H2z"/></svg></div>
    info@thedunlokegroom.com
  </div>
  <div class="footer-rule"></div>
  <div class="footer-name">The Dunlo<br>Hearth &amp; Keg Room</div>
  <div class="copyright">© <b>The Dunlo Hearth &amp; Keg Room</b> - 2017. All Rights Reserved.</div>
</footer>

</body>
</html>
```